Beauty website banner

We are an Australian beauty website selling mid and high end cosmetics and beauty products.

We need a banner that tells customers they can share their product wishlists with friends to let them know what they want for Christmas.

Target Market(s)

Female, 30-60, white collar

Industry/Entity Type

Cosmetics

Requirements
Must have
• 600 x 150 pixels in size

Words to be as follows, not including the (") of course.

"Share your wishlist with friends and family for Christmas!"

(Then in smaller font) "Just log in to your account, go to your wishlist and click on the ‘share wishlist’ button"

```html
<!DOCTYPE html>
<html lang="en">
<head>
<meta charset="utf-8">
<title>Share Your Wishlist Banner</title>
<link rel="stylesheet" href="https://fonts.googleapis.com/css2?family=Passion+One:wght@400&family=Poiret+One&display=swap">
<style>
  :root {
    --banner-pink: #f9a8f4;
    --portrait-light: #f6f1f3;
    --portrait-mid: #f1d6ec;
    --headline-red: #b3002d;
    --headline-shadow: #3a0010;
    --body-ink: #1f1a1e;
  }
  html, body {
    margin: 0;
    padding: 0;
    overflow: hidden;
    background: #ffffff;
  }
  .banner {
    position: relative;
    width: 1200px;
    height: 300px;
    overflow: hidden;
    background: var(--banner-pink);
  }
  .banner__portrait {
    position: absolute;
    left: 0;
    top: 0;
    width: 520px;
    height: 300px;
    background:
      linear-gradient(90deg,
        var(--portrait-light) 0%,
        var(--portrait-light) 35%,
        var(--portrait-mid) 65%,
        rgba(249, 168, 244, 0) 100%);
  }
  .banner__headline {
    position: absolute;
    left: 440px;
    top: 14px;
    width: 600px;
    margin: 0;
    text-align: center;
    font-family: "Passion One", "Arial Black", sans-serif;
    font-weight: 400;
    font-size: 34px;
    line-height: 52px;
    letter-spacing: 0.5px;
    text-transform: uppercase;
    color: var(--headline-red);
    text-shadow: 1px 1px 0 var(--headline-shadow), 2px 2px 3px rgba(58, 0, 16, 0.45);
  }
  .banner__steps {
    position: absolute;
    left: 0;
    top: 0;
    margin: 0;
    font-family: "Poiret One", "Century Gothic", sans-serif;
    font-size: 29px;
    line-height: 1;
    color: var(--body-ink);
    white-space: nowrap;
  }
  .banner__step {
    position: absolute;
    display: block;
  }
  .banner__step--first {
    left: 536px;
    top: 184px;
  }
  .banner__step--second {
    left: 326px;
    top: 224px;
  }
</style>
</head>
<body>
  <div class="banner">
    <div class="banner__portrait" role="img" aria-label="Soft close-up beauty photograph of a woman's closed eye with long dark lashes, fading into pink"></div>
    <h1 class="banner__headline">Share your wishlist with friends and family<br>for Christmas!</h1>
    <p class="banner__steps">
      <span class="banner__step banner__step--first">Just log in to your account</span>
      <span class="banner__step banner__step--second">go to your wishlist and click on the ‘share wishlist’ button</span>
    </p>
  </div>
</body>
</html>
```